New Hire Training Collateral Package ( 6 8.5 x 11 flyer designs)

I'm part of a start up company that has just received a tremendous opportunity that will ultimately allow us to grow our business exponentially (we're really excited) With that in mind, I've been tasked with building our the new hire training program. Imagine your first day at a new company; what are some of the things you need to know.. the core values, mission, vision and values, who your clients and coworkers are... the task is essentially endless HOWEVER ultimately (without scaring them away) the designs should be fun light and exciting! I'm looking for someone to help me grow that vision. See color scheme and original plan in tact. I really liked where these were going and then I lost all our files.. (rookie mistake)

Target Market(s)

Employess

Industry/Entity Type

Financial Service

Font styles to use
Sans Serif

Colors
33b8a4
000000
ffffff

Requirements
Must have
• I'm new to explaining what I want in this format but I believe the below should help: I am looking for a single letter sized flyer for the flyer titles I name below. One for each. You'd be helping me create the templates so I can enter any additional information needed in the text should anything change or need to be altered per employee.
• NEEDS: letter sized flyer (think a normal sized sheet of printer paper), please make sure the page layout is set to 8.5"x11".
• Core Values
• Mission, Vision and Values - A tempate doesn't exist yet
• Employee Profile (Meet the Team)
• Team Hierarchy (Who Rules)
• Company History (Milestone)
• Client Information Doc
• FONTS AND COLORS BELOW
• Aqua
• R: 80
• G: 227
• B: 227
• A: 100
• Hex: 50EE3
• Dark Teal:
• R: 5
• G: 92
• B: 117
• A: 100
• Hex: 055C75
• White:
• R: 225
• G: 225
• B: 225
• A: 100
• Hex: FFF
• Black:
• R: 0
• G: 0
• B: 0
• A: 100
• (pops of color like i have in the flyer examples attached can be included)
• Font: Roboto
Nice to have
• Other suggestions welcome!

```html
<!DOCTYPE html>
<html lang="en">
<head>
<meta charset="utf-8">
<title>Core Values and Mission, Vision &amp; Values Flyers</title>
<link href="https://fonts.googleapis.com/css2?family=Roboto:wght@300;400;500&family=Roboto+Condensed:wght@300;400;700&display=swap" rel="stylesheet">
<style>
  :root{
    --board-light:#ffffff;
    --board-dark:#8c8c8c;
    --ink:#111111;
    --white:#ffffff;
    --dark-teal:#055c75;
    --aqua:#15c6d2;
    --lavender:#a8a9f4;
    --pink:#fb7fc9;
    --green:#0cbf9f;
    --band:#17c8d2;
    --grey-title:#6a7174;
    --body-grey:#3b3f41;
    --vision:#16b3c4;
    --values:#22b9a6;
    --piece-dark:#0a6d8c;
    --piece-mid:#17b5c6;
    --piece-light:#3cc4b0;
  }
  *{margin:0;padding:0;box-sizing:border-box;}
  html,body{width:1200px;height:898px;overflow:hidden;}
  body{
    position:relative;
    background:radial-gradient(ellipse at 50% 45%, var(--board-light) 0%, #c9c9c9 45%, var(--board-dark) 100%);
    font-family:"Roboto",Arial,sans-serif;
  }
  .board-label{
    position:absolute;top:108px;
    font-family:"Roboto Condensed",Arial,sans-serif;font-weight:700;
    font-size:35px;color:var(--ink);letter-spacing:.2px;
    transform:translateX(-50%);white-space:nowrap;
  }
  .label-core{left:361px;}
  .label-mission{left:888px;top:112px;}

  .flyer{
    position:absolute;top:181px;width:461px;height:596px;
    box-shadow:0 6px 18px rgba(0,0,0,.35);overflow:hidden;
  }
  .flyer-core{left:117px;background:var(--white);}
  .flyer-mvv{left:650px;background:linear-gradient(180deg,#c8d1d5 0%,#e6eaeb 55%,#f8f9f9 100%);}

  .brand{
    position:absolute;font-family:"Roboto",Arial,sans-serif;font-weight:400;
    color:var(--dark-teal);letter-spacing:3px;white-space:nowrap;
  }
  .brand-top{top:12px;left:0;width:100%;text-align:center;font-size:14px;}
  .brand-bottom{top:570px;left:343px;font-size:8px;letter-spacing:1.6px;}

  .icon{position:absolute;}
  .value-card{
    position:absolute;border-radius:12px;color:var(--white);padding:14px 13px 0;
  }
  .value-card h3{
    font-family:"Roboto Condensed",Arial,sans-serif;font-weight:700;font-size:15px;
    text-align:center;margin-bottom:8px;letter-spacing:.2px;
  }
  .value-card p{
    font-family:"Roboto Condensed",Arial,sans-serif;font-weight:400;font-size:8.3px;
    line-height:10px;text-align:justify;
  }
  .card-integrity{left:13px;top:116px;width:136px;height:197px;background:var(--aqua);}
  .card-communication{left:162px;top:116px;width:136px;height:197px;background:var(--lavender);}
  .card-service{left:310px;top:116px;width:136px;height:197px;background:var(--pink);}
  .card-newfangled{left:97px;top:356px;width:254px;height:135px;background:var(--green);padding:18px 14px 0;}
  .card-newfangled h3{margin-bottom:9px;}
  .card-newfangled p{font-size:9px;line-height:11px;}

  .drives-band{
    position:absolute;left:0;top:508px;width:100%;height:88px;background:var(--band);
    color:var(--white);padding:7px 13px 0;
  }
  .drives-band h2{
    font-family:"Roboto Condensed",Arial,sans-serif;font-weight:400;font-size:20px;
    text-align:center;margin-bottom:5px;
  }
  .drives-band p{font-family:"Roboto Condensed",Arial,sans-serif;font-size:8.8px;line-height:11.3px;}

  .mvv-title{
    position:absolute;top:14px;left:0;width:100%;text-align:center;
    font-family:"Roboto Condensed",Arial,sans-serif;font-weight:300;font-size:29px;
    color:var(--grey-title);
  }
  .statement{position:absolute;}
  .statement h3{
    font-family:"Roboto Condensed",Arial,sans-serif;font-weight:400;font-size:19px;line-height:20px;
  }
  .statement p{
    font-family:"Roboto Condensed",Arial,sans-serif;font-size:7.1px;line-height:9px;
    color:var(--body-grey);text-align:justify;margin-top:2px;
  }
  .statement-mission{left:53px;top:72px;width:126px;}
  .statement-mission h3{color:var(--dark-teal);}
  .statement-vision{left:283px;top:83px;width:126px;}
  .statement-vision h3{color:var(--vision);}
  .statement-values{left:163px;top:512px;width:148px;}
  .statement-values h3{color:var(--values);}

  .connectors{position:absolute;left:0;top:0;}
  .piece{position:absolute;border-radius:6px;}
  .piece-mission{left:83px;top:183px;width:160px;height:180px;background:linear-gradient(135deg,#0d7f9d,var(--piece-dark));}
  .piece-vision{left:251px;top:175px;width:127px;height:164px;background:var(--piece-mid);}
  .piece-values{left:143px;top:343px;width:186px;height:148px;background:linear-gradient(135deg,#48cdb9,var(--piece-light));}
</style>
</head>
<body>

<div class="board-label label-core">CORE VALUES PAGE</div>
<div class="board-label label-mission">MISSION VISSION PAGE</div>

<section class="flyer flyer-core">
  <div class="brand brand-top">THE MERIDIAN GROUP</div>

  <svg class="icon" style="left:57px;top:63px" width="40" height="40" viewBox="0 0 40 40" role="img" aria-label="Integrity icon">
    <circle cx="20" cy="20" r="20" fill="var(--aqua)"/>
  </svg>
  <svg class="icon" style="left:203px;top:60px" width="40" height="46" viewBox="0 0 40 46" role="img" aria-label="Communication icon">
    <circle cx="8" cy="16" r="7" fill="var(--lavender)"/>
    <circle cx="30" cy="7" r="6" fill="var(--lavender)"/>
    <circle cx="28" cy="35" r="9" fill="var(--lavender)"/>
    <line x1="8" y1="16" x2="30" y2="7" stroke="var(--lavender)" stroke-width="1.5"/>
    <line x1="8" y1="16" x2="28" y2="35" stroke="var(--lavender)" stroke-width="1.5"/>
  </svg>
  <svg class="icon" style="left:363px;top:71px" width="34" height="34" viewBox="0 0 34 34" role="img" aria-label="Service icon">
    <rect x="2" y="2" width="30" height="30" rx="4" fill="var(--pink)"/>
  </svg>

  <div class="value-card card-integrity">
    <h3>INTEGRITY</h3>
    <p>This one is a no-brainer. Integrity drives how we work and how we make our decisions on the most basic levels and in the most ubiquitous of ways. Trust, appropriate decision making, and honor are key in every single thing we do so this just make sense as our top value.</p>
  </div>
  <div class="value-card card-communication">
    <h3>COMMUNICATION</h3>
    <p>To us there is no such thing as being “too communicative.” We strive to be scary-fast responsive, but not to the detriment of poise, knowledge, and accuracy. We aim to collaborate and we are not afraid to ask questions. Working in a remote capacity and aiming to provide the feel of an in-house employee, it is important we stay communicative as possible. So we made is part of who we are. Ultimately, this is who we are…a service company.</p>
  </div>
  <div class="value-card card-service">
    <h3>SERVICE</h3>
    <p>We want our clients to feel we are in this together and simply put, it’s because we are. Our goals aren’t just problem solving and completing tasks. It’s about making sure the person we are serving gets what they’re looking for and more! We want to go above and beyond in respect and courteousness, maintain a high level of empathy, and always remember to take the initiative.</p>
  </div>

  <svg class="icon" style="left:210px;top:323px" width="36" height="34" viewBox="0 0 36 34" role="img" aria-label="Newfangled icon">
    <circle cx="20" cy="10" r="8" fill="var(--green)"/>
    <rect x="2" y="22" width="32" height="8" rx="4" fill="var(--green)"/>
  </svg>

  <div class="value-card card-newfangled">
    <h3>NEWFANGLED</h3>
    <p>(not even a noun in this context like the rest of our values)? Well so are we… kind of. It’s defined as objectively new or different to be exact. We encourage our staff to think outside the box… how can we set ourselves apart? One of the great things about our company and our team is that we do things a bit</p>
  </div>

  <div class="drives-band">
    <h2>WHAT DRIVES US?</h2>
    <p>At The Meridian Group, we want to always do the best, be our best, and exemplify the best. Easier said than done and not always easy to figure what that means in plain English. So here is our cheesy, but genuine description of the culture that we strive to create, nurture, and uphold day in and day out..</p>
  </div>
</section>

<section class="flyer flyer-mvv">
  <h1 class="mvv-title">MISSION, VISION &amp; VALUES</h1>

  <div class="statement statement-mission">
    <h3>MISSION</h3>
    <p>Neque porro quisquam est qui dolorem ipsum quia dolor sit amet, consectetur, adipisci velit. There is no one who loves pain itself, who seeks after it and wants to have it, simply because it is pain.</p>
  </div>
  <div class="statement statement-vision">
    <h3>VISION</h3>
    <p>Neque porro quisquam est qui dolorem ipsum quia dolor sit amet, consectetur, adipisci velit. There is no one who loves pain itself, who seeks after it and wants to have it, simply because it is pain.</p>
  </div>

  <div class="piece piece-mission" role="img" aria-label="Dark teal puzzle piece for mission"></div>
  <div class="piece piece-vision" role="img" aria-label="Aqua puzzle piece for vision"></div>
  <div class="piece piece-values" role="img" aria-label="Green puzzle piece for values"></div>

  <svg class="connectors" width="461" height="596" viewBox="0 0 461 596">
    <polyline points="179,142 50,142 50,249" fill="none" stroke="var(--dark-teal)" stroke-width="1.6" stroke-dasharray="1.6 2.4"/>
    <circle cx="179" cy="142" r="4" fill="var(--dark-teal)"/>
    <circle cx="50" cy="249" r="4" fill="var(--dark-teal)"/>
    <polyline points="277,152 409,152 409,263" fill="none" stroke="var(--vision)" stroke-width="1.6" stroke-dasharray="1.6 2.4"/>
    <circle cx="277" cy="152" r="4" fill="var(--vision)"/>
    <circle cx="409" cy="263" r="4" fill="var(--vision)"/>
    <polyline points="166,482 166,506 309,506 309,482" fill="none" stroke="var(--values)" stroke-width="1.6" stroke-dasharray="1.6 2.4"/>
    <circle cx="166" cy="482" r="4" fill="var(--values)"/>
    <circle cx="309" cy="482" r="4" fill="var(--values)"/>
  </svg>

  <div class="statement statement-values">
    <h3>VALUES</h3>
    <p>Neque porro quisquam est qui dolorem ipsum quia dolor sit amet, consectetur, adipisci velit. There is no one who loves pain itself, who seeks after it and wants to have it, simply because it is pain.</p>
  </div>

  <div class="brand brand-bottom">THE MERIDIAN GROUP</div>
</section>

</body>
</html>
```